upgrade old website to new wordpress website

Looking to have kwrmedbill.com upgraded to a new wordpress website utilizing much of the content already present. While still pairing down or presenting differently the current information. Clean design with no fast moving or difficult to navigate links or pages. Looking for blog type space for tips on billing issues found and work arounds for the issues. Want to update monthly or less. Link to show website of our software vendor available for some clients to demonstrate amount of software options available (www.vantorimed.com). Do not want anyone to Leave our site, just have access to see the other site. More captions or area of interest to describe specific types of providers we bill for. IE: ambulance, ambulette, Ems go together and we have experience in partnering and billing with Brek data & Medvo pad software amoung others. 40 Yr experience in Chiropractic billing especially Workers Comp and Auto. 96% collections for Certified Nurse Practitioners and Physical therapists. Rest of pages should explain our experience, another for our percentage of collection results for providers. Another for our credentialing experience and services. Another for our Management services. Some type of contact for more information that requests the type of provider they are and what they are looking for .

Target Market(s)

Client information and front face of company.

Coding

Coded - Design and coding required

Number of Pages Required

5+ page

Font styles to use
Sans Serif

Requirements
Must have
• Be compatible with tablets and regular computers. Ability to upload to my own webhost and information blocks that can be updated if needed in future. Wining page upgradable and fully functional.
Nice to have
• Small blog update section, blurbs for information, additional pages for more in depth information. Cleaner look to pages and theme.
Should not have
• Difficult to find pages or hidden information

```html
<!DOCTYPE html>
<html lang="en">
<head>
<meta charset="utf-8">
<title>K.W.R. Health Services</title>
<link href="https://fonts.googleapis.com/css2?family=Open+Sans:wght@400;600;700&family=Tinos:wght@700&display=swap" rel="stylesheet">
<style>
:root{
  --navy:#1b1653;
  --navy-deep:#15113f;
  --nav-top:#2d279a;
  --nav-bottom:#17124f;
  --ink:#3a3a3a;
  --muted:#777;
  --rule:#e4e4e4;
  --footer:#1f1f1f;
  --footer-bottom:#151515;
  --footer-text:#a8a8a8;
  --star:#e8a31c;
}
*{box-sizing:border-box;margin:0;padding:0}
html,body{width:1200px;height:2323px;overflow:hidden;background:#fff}
body{font-family:"Open Sans",Arial,sans-serif;color:var(--ink);position:relative}
a{color:inherit;text-decoration:none}
.top-rule{position:absolute;left:0;top:0;width:1200px;height:4px;background:var(--navy)}
.brand{position:absolute;left:100px;top:34px;font-family:"Open Sans",Arial,sans-serif;font-weight:700;font-size:26px;color:var(--navy);border-bottom:2px solid var(--navy);padding-bottom:2px}
.phone{position:absolute;right:98px;top:46px;font-size:17px;font-weight:600;color:var(--navy);display:flex;align-items:center;gap:12px}
.main-nav{position:absolute;left:100px;top:99px;width:1002px;height:53px;background:linear-gradient(var(--nav-top),var(--nav-bottom));display:flex;align-items:center;padding-left:32px}
.main-nav a{color:#fff;font-size:12px;letter-spacing:.2px;margin-right:60px}
.search{position:absolute;right:10px;top:9px;width:208px;height:33px;background:#fff;border-radius:2px;display:flex;align-items:center;justify-content:space-between;padding:0 10px;font-size:11px;font-style:italic;color:#999}
.hero{position:absolute;left:100px;top:162px;width:1002px;height:474px;background:radial-gradient(ellipse at 50% 40%,#4a3a30 0%,#1d1b1c 45%,#0b0b0c 100%);box-shadow:0 30px 30px -20px rgba(0,0,0,.35)}
.hero-title{position:absolute;left:593px;top:360px;color:#fff;font-size:26px;font-weight:600;line-height:40px}
.hero-dots{position:absolute;left:477px;top:429px;display:flex;gap:6px}
.hero-dots span{width:10px;height:10px;border-radius:50%;background:#fff}
.welcome{position:absolute;left:0;width:1200px;top:682px;text-align:center;font-size:27px;color:#777}
.welcome b{font-weight:400;color:var(--navy)}
.divider{position:absolute;left:100px;top:745px;width:1002px;height:1px;background:var(--rule)}
.divider::after{content:"";position:absolute;left:493px;top:-3px;width:16px;height:6px;border:1px solid var(--rule);background:#fff}
.different{position:absolute;left:0;width:1200px;top:769px;text-align:center;font-size:15px;font-weight:600;color:var(--navy)}
.intro{position:absolute;left:122px;width:958px;top:807px;text-align:center;font-size:11.5px;line-height:21px;color:#555}
.management{position:absolute;left:0;top:919px;width:1200px;height:411px;background:var(--navy)}
.management h2{position:absolute;width:100%;top:26px;text-align:center;color:#fff;font-weight:400;font-size:21px}
.service{position:absolute;top:80px;width:220px;text-align:center;color:#fff}
.service .ring{width:146px;height:146px;margin:0 auto;border-radius:50%;border:5px solid #fff;display:flex;align-items:center;justify-content:center}
.service h3{font-weight:400;font-size:15px;margin-top:28px}
.service p{font-size:11.5px;line-height:20px;margin-top:9px;padding:0 12px}
.service a{display:inline-block;margin-top:14px;font-size:11.5px;text-decoration:underline}
.section-title{position:absolute;left:0;width:1200px;text-align:center;font-size:21px;color:#777}
.section-title b{font-weight:600;color:var(--navy)}
.billing-card{position:absolute;top:1423px;width:312px;height:199px;box-shadow:0 22px 22px -18px rgba(0,0,0,.35)}
.billing-card .photo{width:100%;height:100%;background:linear-gradient(135deg,#e9ecef,#b9c0c8 60%,#59606a)}
.billing-card .caption{position:absolute;left:0;bottom:0;width:100%;height:47px;background:rgba(45,37,140,.88);color:#fff;font-size:15px;padding:16px 0 0 14px}
.col-title{position:absolute;font-size:20px;color:#333}
.blog-item{position:absolute;left:100px;width:320px;height:70px}
.blog-item .thumb{position:absolute;left:0;top:0;width:94px;height:68px;background:linear-gradient(135deg,#c9ccd0,#4c525a)}
.blog-item .body{position:absolute;left:103px;top:-2px;font-size:11.5px;line-height:18px;color:#555}
.blog-item h4{font-weight:400;font-size:12px;color:#444}
.blog-item a{color:#2a3d9a}
.avatar{position:absolute;left:463px;top:1762px;width:136px;height:136px;border-radius:50%;border:4px solid #fff;box-shadow:0 0 0 1px #ddd;background:radial-gradient(circle at 50% 40%,#d9dde2,#6c7684)}
.quote{position:absolute;left:650px;top:1776px;width:380px;font-size:11.5px;line-height:19px;color:#555;padding-left:28px}
.quote .mark{position:absolute;font-size:22px;font-weight:700;color:#333}
.stars{position:absolute;left:623px;top:1844px;font-size:13px;letter-spacing:1px;color:var(--star)}
.stars span{color:#bbb}
.client{position:absolute;left:623px;top:1886px;font-size:13px;font-weight:600;color:var(--navy)}
.site-footer{position:absolute;left:0;top:1968px;width:1200px;height:286px;background:var(--footer);color:var(--footer-text)}
.site-footer h5{position:absolute;top:30px;font-size:20px;font-weight:400;color:#fff}
.site-footer ul{position:absolute;top:69px;list-style:none;font-size:11.5px;line-height:20.5px}
.newsletter-note{position:absolute;left:100px;top:67px;width:250px;font-size:11.5px;line-height:20px}
.email{position:absolute;left:100px;top:128px;width:245px;height:46px;background:#fff;color:#222;font-size:14px;padding:14px 15px}
.signup{position:absolute;left:100px;top:201px;width:84px;height:40px;background:#000;color:#fff;font-size:14px;font-weight:600;text-align:center;line-height:40px;border-radius:2px}
.social li{display:flex;align-items:center;gap:7px}
.social i{width:9px;height:9px;background:#bbb;display:inline-block}
.copyright{position:absolute;left:0;top:2254px;width:1200px;height:69px;background:var(--footer-bottom);color:#fff;font-size:12px;text-align:center;line-height:69px}
.copyright .code{position:absolute;right:36px;top:0}
</style>
</head>
<body>
<div class="top-rule"></div>
<header>
  <div class="brand">K.W.R. Health Services</div>
  <div class="phone">
    <svg width="16" height="16" viewBox="0 0 24 24"><path fill="#999" d="M6.6 10.8a15 15 0 0 0 6.6 6.6l2.2-2.2a1 1 0 0 1 1-.25 11.4 11.4 0 0 0 3.6.57 1 1 0 0 1 1 1V20a1 1 0 0 1-1 1A17 17 0 0 1 3 4a1 1 0 0 1 1-1h3.5a1 1 0 0 1 1 1c0 1.25.2 2.45.57 3.57a1 1 0 0 1-.25 1z"/></svg>
    (555)-014-2230
  </div>
  <nav class="main-nav">
    <a href="#">HOME</a><a href="#">BILLING SERVICES</a><a href="#">MANAGEMENT SERVICES</a><a href="#">ABOUT US</a><a href="#">LINKS</a><a href="#">CONTACT</a>
    <div class="search">Search...
      <svg width="14" height="14" viewBox="0 0 24 24"><circle cx="10" cy="10" r="7" fill="none" stroke="#555" stroke-width="2.5"/><line x1="15" y1="15" x2="21" y2="21" stroke="#555" stroke-width="2.5"/></svg>
    </div>
  </nav>
</header>

<section class="hero" role="img" aria-label="Two business people in suits shaking hands on a dark background">
  <h1 class="hero-title">KWR Health Services - Defining<br>Great Practices</h1>
  <div class="hero-dots"><span></span><span></span><span></span></div>
</section>

<h2 class="welcome">Welcome To <b>K.W.R Health&nbsp; Services</b></h2>
<div class="divider"></div>
<h3 class="different">WHAT MAKES US DIFFERENT.</h3>
<p class="intro">KWR Health Services&nbsp; has been billing for Healthcare providers, Chiropractic, Ambulance and EMS&nbsp; providers since 1978, and has over 30 years of experience in owning and operating multiple health care clinics. All of our staff has a minimum experience of&nbsp; 15 years each in health care billing. We attend many Medicare, Medicaid and private insurance seminars each year, as well as many specialty provider organizations such as the Lakeview Ambulance Transport Assoc., Midland State Medical Assoc, Midland State Chiropractic Assoc. etc.&nbsp; We also attend OSHA, BWC, Collections seminars, coding, office management and HIPAA seminars as new information becomes available.</p>

<section class="management">
  <h2>Management Service</h2>
  <div class="service" style="left:108px">
    <div class="ring"><svg width="64" height="52" viewBox="0 0 64 52" fill="none" stroke="#fff" stroke-width="6" stroke-linecap="round"><path d="M6 18a37 37 0 0 1 52 0"/><path d="M16 28a23 23 0 0 1 32 0"/><path d="M25 37a10 10 0 0 1 14 0"/><circle cx="32" cy="46" r="2" fill="#fff"/></svg></div>
    <h3>APPEALS</h3>
    <p>Automatically filed, Tracked through provider offices and insurance companies.</p>
    <a href="#">READ MORE</a>
  </div>
  <div class="service" style="left:361px">
    <div class="ring"><svg width="70" height="60" viewBox="0 0 70 60"><g fill="#fff"><circle cx="26" cy="32" r="15"/><circle cx="52" cy="16" r="9"/><circle cx="52" cy="46" r="9"/></g><g stroke="#fff" stroke-width="7"><path d="M26 10v44M4 32h44M10 16l32 32M42 16L10 48"/><path d="M52 3v26M39 16h26M52 33v26M39 46h26" stroke-width="5"/></g><g fill="#1b1653"><circle cx="26" cy="32" r="6"/><circle cx="52" cy="16" r="3.5"/><circle cx="52" cy="46" r="3.5"/></g></svg></div>
    <h3>CODING</h3>
    <p>Pellentesque et lacus pretium tinunt. Pellentesque at metus. Donec nisl a nisl. Vestibulum ante ipsum</p>
    <a href="#">READ MORE</a>
  </div>
  <div class="service" style="left:607px">
    <div class="ring"><svg width="66" height="54" viewBox="0 0 66 54" fill="none" stroke="#fff" stroke-width="5"><path d="M4 2v48h60"/><path d="M12 40l14-14 10 10 20-22"/><path d="M46 12h12v12" stroke-linejoin="miter"/></svg></div>
    <h3>PATIENT ACCOUNTS</h3>
    <p>Pellentesque et lacus pretium tinunt. Pellentesque at metus. Donec nisl a nisl. Vestibulum ante ipsum</p>
    <a href="#">READ MORE</a>
  </div>
  <div class="service" style="left:861px">
    <div class="ring"><svg width="56" height="58" viewBox="0 0 56 58" fill="none" stroke="#fff" stroke-width="5"><path d="M8 30v22h32V30"/><path d="M8 40h32M8 30h32"/><path d="M20 22l22-6M24 14l16-10M34 8l12-6" stroke-linecap="round"/></svg></div>
    <h3>PATIENT STATEMENTS</h3>
    <p>Pellentesque et lacus pretium tinunt. Pellentesque at metus. Donec nisl a nisl. Vestibulum ante ipsum</p>
    <a href="#">READ MORE</a>
  </div>
</section>

<h2 class="section-title" style="top:1360px">Billing <b>Services</b></h2>
<article class="billing-card" style="left:100px"><div class="photo" role="img" aria-label="Trainer presenting at a whiteboard to staff around a table"></div><div class="caption">*Staff Training</div></article>
<article class="billing-card" style="left:444px"><div class="photo" role="img" aria-label="Colleagues meeting around a desk in a bright office"></div><div class="caption">Provider Enrollment</div></article>
<article class="billing-card" style="left:790px"><div class="photo" role="img" aria-label="Business team reviewing documents together"></div><div class="caption">Provider Credentials</div></article>

<h3 class="col-title" style="left:100px;top:1683px">Latest Blog Post</h3>
<article class="blog-item" style="top:1740px">
  <div class="thumb" role="img" aria-label="Person working on a laptop outdoors"></div>
  <div class="body"><h4>Featured Blog Tittle</h4>Morbi diam mauris viverra in gravida eu<br>mattis in ante Morbi eget arcu Morbi porta<br><a href="#">Read More</a></div>
</article>
<article class="blog-item" style="top:1844px">
  <div class="thumb" role="img" aria-label="Businessman pointing at a screen"></div>
  <div class="body"><h4>Featured Blog Tittle</h4>Morbi diam mauris viverra in gravida eu<br>mattis in ante Morbi eget arcu Morbi porta<br><a href="#">Read More</a></div>
</article>

<h3 class="col-title" style="left:475px;top:1688px">Testimonials</h3>
<div class="avatar" role="img" aria-label="Portrait of the client giving the testimonial"></div>
<blockquote class="quote">
  <span class="mark" style="left:0;top:-8px">&ldquo;</span>
  Nulla sollicitudin tincidunt dui et egestas. Phasellus non sem tum, ullamcorper vitae, accumsan dui. Duis dignissim condi lorem. Maecenas facilisis ipsum sed porttitor rutrum.
  <span class="mark" style="left:192px;top:44px">&rdquo;</span>
</blockquote>
<div class="stars">★★★<span>☆☆</span></div>
<div class="client">EVAN MARLOW</div>

<footer class="site-footer">
  <h5 style="left:100px">Subscribe Our Newsletter</h5>
  <p class="newsletter-note">Register for diabetes news, research and food &amp; fitness tips.</p>
  <div class="email">Enter Your Email Id</div>
  <div class="signup">Sign up</div>
  <h5 style="left:437px">Who We Are</h5>
  <ul style="left:437px"><li>About</li><li>Mission</li><li>Values</li><li>Our Work</li><li>Board Members</li><li>Financials</li><li>Contact Info</li><li>Staff</li></ul>
  <h5 style="left:626px">Company</h5>
  <ul style="left:631px"><li>CHRONIC KIDNEY DISEASE</li><li>PATIENT &amp; FAMILY</li><li>RESOURCES</li><li>DONATE</li></ul>
  <h5 style="left:830px">Our Area</h5>
  <ul style="left:834px"><li>EDUCATION</li><li>ADVOCACY</li><li>JOIN US</li><li>CONTACT US</li></ul>
  <h5 style="left:1000px">Find Us On</h5>
  <ul class="social" style="left:1001px"><li><i></i>Circlebook</li><li><i></i>Chirper</li><li><i></i>Rss</li><li><i></i>ViewTube</li></ul>
</footer>
<div class="copyright">© 2015 kwrmedbill. All Right Reserved<span class="code">D4</span></div>
</body>
</html>
```